We need a poster design for "KEVO Sports Night" events. The events have been around for 3 years and we hope the poster will give a sense of vibrant and active designs. It is more to a community event with teamwork and fun.

I have uploaded a past event poster just FYI.

Target Market(s)

Community, Family

Industry/Entity Type

Non Profit

Logo Text

KEVO Sports Night

Requirements
Must have
• KEVO Sports Night
• Organiser: KEVO Sydney
• Date: 25/11/2017
• Time: 4:00pm
• Venue: Wendamere Park
• Facebook: kevosport

```html
<!DOCTYPE html>
<html lang="en">
<head>
<meta charset="utf-8">
<title>KEVO Sports Night</title>
<link rel="stylesheet" href="https://fonts.googleapis.com/css2?family=Montserrat:ital,wght@1,900&family=Oswald:wght@400;500;600&family=Roboto:ital,wght@1,500&display=swap">
<style>
  :root {
    --stage: #efefef;
    --paper: #ffffff;
    --sky: #e4e8ee;
    --sky-deep: #cfd6e0;
    --navy: #2b2a6b;
    --violet: #6a2a9a;
    --magenta: #9a2a8e;
    --ink: #1e1e28;
    --red: #b8262b;
    --band: rgba(255,255,255,0.82);
    --splash-yellow: rgba(246,236,120,0.75);
    --splash-red: rgba(226,70,62,0.7);
    --skin: rgba(150,110,95,0.55);
  }
  * { margin: 0; padding: 0; box-sizing: border-box; }
  html, body { width: 1026px; height: 1200px; overflow: hidden; background: var(--stage); }

  .poster {
    position: absolute; left: 95px; top: 0;
    width: 836px; height: 1200px;
    background: var(--paper);
    padding: 15px;
  }
  .poster-field {
    position: relative; width: 100%; height: 100%; overflow: hidden;
    background:
      radial-gradient(circle at 22% 16%, rgba(255,255,255,0.95) 0 70px, transparent 72px),
      radial-gradient(circle at 80% 28%, rgba(255,255,255,0.7) 0 45px, transparent 47px),
      radial-gradient(circle at 14% 40%, rgba(255,255,255,0.6) 0 55px, transparent 57px),
      radial-gradient(circle at 90% 80%, rgba(255,255,255,0.6) 0 40px, transparent 42px),
      radial-gradient(ellipse at 50% 45%, #f4f6f9 0%, var(--sky) 60%, var(--sky-deep) 100%);
  }
  .streaks { position: absolute; inset: 0; width: 100%; height: 100%; }

  .runner-art {
    position: absolute; left: 20px; top: 103px; width: 710px; height: 1018px;
    background:
      radial-gradient(ellipse 140px 90px at 24% 18%, var(--splash-yellow), transparent 70%),
      radial-gradient(ellipse 150px 120px at 60% 48%, var(--splash-red), transparent 72%),
      radial-gradient(ellipse 260px 460px at 42% 45%, var(--skin), transparent 70%);
  }

  .band {
    position: absolute; background: var(--band);
    transform: rotate(-6deg); transform-origin: center;
  }
  .band-1 { left: 125px; top: 360px; width: 610px; height: 88px; }
  .band-2 { left: 145px; top: 520px; width: 620px; height: 80px; }
  .band-3 { left: 75px; top: 655px; width: 640px; height: 90px; }

  .title {
    position: absolute; left: 0; top: 0; width: 100%;
    font-family: "Montserrat", sans-serif; font-weight: 900; font-style: italic;
    color: var(--navy); letter-spacing: -3px; line-height: 1;
    text-transform: uppercase;
  }
  .title-line { position: absolute; display: block; font-size: 142px; transform: rotate(-6deg); transform-origin: left center; white-space: nowrap; }
  .title-brand {
    left: 225px; top: 345px;
    background: linear-gradient(90deg, var(--magenta), var(--violet) 50%, var(--navy));
    -webkit-background-clip: text; background-clip: text; color: transparent;
  }
  .title-sports { left: 95px; top: 478px; }
  .title-night { left: 150px; top: 605px; }

  .details {
    position: absolute; left: 492px; top: 850px; width: 282px;
    font-family: "Oswald", sans-serif; color: var(--ink); text-transform: uppercase;
  }
  .organiser {
    display: flex; align-items: center; gap: 8px;
    font-size: 28px; font-weight: 500; letter-spacing: 1px; line-height: 1.3;
  }
  .organiser::before, .organiser::after { content: ""; height: 3px; background: var(--ink); width: 18px; }
  .organiser::after { flex: 1; }
  .date { display: flex; align-items: flex-start; margin-top: 4px; line-height: 1; }
  .date-month { font-size: 78px; font-weight: 500; }
  .date-day { font-size: 86px; font-weight: 500; color: var(--red); margin-left: 4px; }
  .date-side { display: flex; flex-direction: column; margin-left: 4px; }
  .date-suffix { font-size: 48px; color: var(--red); font-weight: 500; }
  .date-year { font-size: 22px; font-weight: 600; margin-top: 4px; }
  .time {
    position: relative; display: flex; align-items: center; gap: 10px;
    font-size: 54px; font-weight: 500; line-height: 1; margin-top: 6px; padding-left: 16px;
  }
  .time::before {
    content: ""; position: absolute; left: 0; top: -6px; width: 12px; height: 36px;
    border-left: 3px solid var(--ink); border-bottom: 3px solid var(--ink);
  }
  .time::after { content: ""; flex: 1; height: 3px; background: var(--ink); }
  .venue {
    font-size: 34px; font-weight: 500; color: var(--red); margin-top: 10px;
    letter-spacing: 1px; line-height: 1.3; white-space: nowrap;
  }
  .social {
    display: flex; align-items: center; justify-content: flex-end; gap: 8px;
    margin-top: 4px; font-family: "Roboto", sans-serif; font-style: italic; font-weight: 500;
    font-size: 21px; line-height: 1.3; text-transform: none; color: var(--navy);
  }
  .social-dot { width: 12px; height: 12px; border-radius: 50%; background: var(--navy); }
</style>
</head>
<body>
  <div class="poster">
    <div class="poster-field">
      <div class="runner-art" role="img" aria-label="Photo of a sprinter running to the right with yellow and red paint splashes"></div>
      <svg class="streaks" viewBox="0 0 806 1170" aria-hidden="true">
        <line x1="40" y1="1050" x2="760" y2="120" stroke="#fff" stroke-width="2" opacity="0.9"/>
        <line x1="300" y1="1160" x2="806" y2="520" stroke="#fff" stroke-width="1.5" opacity="0.8"/>
        <line x1="0" y1="660" x2="420" y2="120" stroke="#fff" stroke-width="1" opacity="0.6"/>
      </svg>
      <div class="band band-1"></div>
      <div class="band band-2"></div>
      <div class="band band-3"></div>
      <h1 class="title">
        <span class="title-line title-brand">KEVO</span>
        <span class="title-line title-sports">Sports</span>
        <span class="title-line title-night">Night</span>
      </h1>
      <div class="details">
        <p class="organiser">KEVO Sydney</p>
        <p class="date">
          <span class="date-month">Nov</span>
          <span class="date-day">25</span>
          <span class="date-side"><span class="date-suffix">th</span><span class="date-year">2017</span></span>
        </p>
        <p class="time">4:00 PM</p>
        <p class="venue">Wendamere Park</p>
        <p class="social"><span class="social-dot"></span>kevosport</p>
      </div>
    </div>
  </div>
</body>
</html>
```